Tolvane Air and Electrical Website

Simple and easy to use website for a Electrical and Air Conditioning contracting business.Use stock photosOnline contact portallogo still to be supplied

Target Market(s)

Mums and Dads who want a local contractor

Coding

Coded - Design and coding required

Number of Pages Required

2 page

Font styles to use
Sans Serif

Colors
f04a50
3276b5
33a6d7

Requirements
Must have
• Simple and easy to use
• Ph number
• 4 web address; linked to page
• 0417385926
• tolvane.com.au
• tolvaneelectrical.com.au
• tolvaneairandelectrical.com.au
• tolvaneair.com.au
Nice to have
• Split System Air Con Picture
• Electrical Pictures

```html
<!DOCTYPE html>
<html lang="en">
<head>
<meta charset="utf-8">
<title>Tolvane Air and Electrical</title>
<link href="https://fonts.googleapis.com/css2?family=Varela+Round&family=Arimo:wght@400;700&display=swap" rel="stylesheet">
<style>
:root{
  --blue:#1a73c6;
  --blue-dark:#145fa6;
  --red:#f0292d;
  --ink:#222;
  --muted:#555;
  --topbar:#333;
  --footer:#252525;
  --card:#fafafa;
}
*{box-sizing:border-box;margin:0;padding:0}
html,body{width:1200px;height:4000px;overflow:hidden}
body{font-family:"Arimo",sans-serif;color:var(--ink);background:#fff;position:relative}
a{color:inherit;text-decoration:none}
.head{font-family:"Varela Round",sans-serif;letter-spacing:1.5px}
.abs{position:absolute}
.btn{position:absolute;background:var(--blue);color:#fff;border-radius:20px;font-size:14px;display:flex;align-items:center;justify-content:center;height:36px;width:174px}
.ph{position:absolute}

.topbar{position:absolute;left:0;top:0;width:1200px;height:31px;background:var(--topbar);color:#fff;font-size:14px}
.topbar .phone{left:80px;top:8px;display:flex;gap:8px;align-items:center}
.topbar .mail{left:523px;top:8px;display:flex;gap:8px;align-items:center}
.topbar .social{right:70px;top:0;display:flex}
.topbar .social span{width:32px;height:31px;display:flex;align-items:center;justify-content:center}
.topbar .social span i{width:9px;height:9px;background:#fff;display:block;border-radius:2px}
.topbar .social span.on{background:var(--red)}

.brand{position:absolute;display:flex;align-items:center;gap:10px;font-family:"Varela Round",sans-serif;font-size:42px;color:var(--blue)}
.brand b{width:36px;height:36px;background:var(--red);display:block}

.nav{position:absolute;left:0;top:135px;width:1200px;height:40px;background:var(--blue);display:flex;padding-left:80px;font-size:14px;color:#fff}
.nav a{height:40px;display:flex;align-items:center;justify-content:center;border-right:1px solid rgba(255,255,255,.35)}
.nav a.on{background:var(--red)}
.nav .quote{background:var(--red);border-radius:14px;height:28px;margin:6px 0 0 12px;padding:0 32px;border:none}

.hero{left:0;top:175px;width:1200px;height:443px;background:linear-gradient(90deg,#e9e9e9,#f3f3f3 55%,#f7f7f7)}
.hero-title{left:713px;top:310px;font-size:31px;line-height:38px;color:#222}
.hero-text{left:713px;top:412px;width:420px;font-size:13px;line-height:16px;color:#444}

.section-title{font-size:30px;color:#222}
.about-text{left:81px;top:790px;width:505px;font-size:12.5px;line-height:16px;color:#333}
.about-text p{margin-bottom:16px}
.about-frame{left:601px;top:672px;width:519px;height:352px;background:#efefef}

.svc{top:1139px;width:241px;height:243px}
.svc-label{top:1400px;width:241px;text-align:center;font-size:18px;color:#222;line-height:24px}

.cats{left:0;top:1560px;width:1200px;height:534px;background:var(--blue);color:#fff}
.cats h2{position:absolute;left:0;top:36px;width:1200px;text-align:center;font-size:30px;font-weight:400}
.cat-col{position:absolute;top:102px;list-style:none}
.cat-col li{height:38.5px;display:flex;align-items:center;gap:18px;font-size:19px;font-family:"Varela Round",sans-serif;letter-spacing:1.2px}

.t-card{top:2238px;width:320px;height:315px;background:var(--card);text-align:center;border-radius:4px}
.t-card .avatar{width:110px;height:110px;border-radius:50%;margin:34px auto 0}
.t-card .name{margin-top:14px;font-size:18px;font-family:"Varela Round",sans-serif;letter-spacing:1px}
.t-card .role{color:var(--blue);font-size:14px;margin-top:4px}
.t-card .quote{font-size:13px;line-height:16px;color:#666;margin:12px auto 0;width:215px}
.t-card .quote.bold{color:#222;font-weight:700}
.t-card .more{font-size:13px;color:#444;margin-top:14px;display:flex;justify-content:center;gap:8px;align-items:center}

.b-card{top:2702px;width:319px;height:394px;background:#fff;box-shadow:0 0 6px rgba(0,0,0,.06)}
.b-card .img{height:213px}
.b-card .link{position:absolute;left:132px;top:188px;width:50px;height:50px;border-radius:50%;background:var(--blue);border:4px solid #fff;display:flex;align-items:center;justify-content:center}
.b-card .row{position:absolute;left:12px;right:12px;top:266px;display:flex;justify-content:space-between;align-items:baseline}
.b-card .row .t{font-size:18px;font-family:"Varela Round",sans-serif;letter-spacing:1px}
.b-card .row .d{font-size:13px;color:#444}
.b-card .txt{position:absolute;left:12px;right:12px;top:300px;font-size:13px;line-height:18px;color:#444}
.b-card .foot{position:absolute;left:12px;right:12px;top:355px;display:flex;justify-content:space-between;font-size:13px;color:#444}
.b-card .foot u{color:#333}
.b-card .stats{display:flex;gap:16px;color:#444}

.contact{left:0;top:3220px;width:598px;height:435px;background:var(--blue);color:#fff}
.contact h2{position:absolute;left:80px;top:84px;font-size:30px;font-weight:400}
.field{position:absolute;background:var(--blue-dark);font-size:13px;padding:10px 16px;height:36px}
.map{left:598px;top:3220px;width:602px;height:435px;background:linear-gradient(135deg,#e8e6e3,#dcdad6)}
.map-card{left:682px;top:3368px;width:330px;height:108px;background:rgba(255,255,255,.85);font-size:13px;line-height:23px;padding:14px 0 0 58px;color:#222}

.footer{left:0;top:3655px;width:1200px;height:287px;background:var(--footer);color:#fff}
.footer h4{font-family:"Varela Round",sans-serif;font-weight:400;font-size:18px;letter-spacing:.5px}
.footer ul{list-style:disc;padding-left:20px;font-size:12.5px;line-height:17px;margin-top:12px}
.f-contact div{display:flex;gap:16px;font-size:13px;line-height:25px}
.subscribe{display:flex;margin-top:22px;width:226px;height:28px;border:1px solid #fff;border-radius:14px;overflow:hidden;font-size:10px}
.subscribe span{flex:1;display:flex;align-items:center;padding-left:16px}
.subscribe b{background:#fff;color:#333;font-weight:400;width:74px;display:flex;align-items:center;justify-content:center}
.socials{display:flex;gap:10px;margin-top:16px}
.socials i{width:24px;height:24px;border-radius:50%;background:#fff;display:block}
.web-links{left:81px;top:252px;width:1040px;display:flex;gap:28px;font-size:12.5px;color:#cfd8e3}
.web-links a{text-decoration:underline}
.bottom{left:0;top:3942px;width:1200px;height:58px;background:var(--footer);border-top:1px solid #3a3a3a;color:#fff;font-size:13px}
</style>
</head>
<body>

<div class="topbar">
  <div class="abs phone">
    <svg width="14" height="14" viewBox="0 0 24 24"><path fill="#fff" d="M6.6 10.8a15 15 0 0 0 6.6 6.6l2.2-2.2a1 1 0 0 1 1-.25 11.4 11.4 0 0 0 3.6.6 1 1 0 0 1 1 1V20a1 1 0 0 1-1 1A17 17 0 0 1 3 4a1 1 0 0 1 1-1h3.5a1 1 0 0 1 1 1c0 1.25.2 2.45.6 3.6a1 1 0 0 1-.25 1z"/></svg>
    0417385926</div>
  <div class="abs mail">
    <svg width="16" height="12" viewBox="0 0 16 12"><rect x=".5" y=".5" width="15" height="11" fill="none" stroke="#fff"/><path d="M.5.5 8 7l7.5-6.5" fill="none" stroke="#fff"/></svg>
    info@tolvane.com</div>
  <div class="abs social"><span><i></i></span><span class="on"><i></i></span><span><i></i></span><span><i></i></span><span><i></i></span></div>
</div>

<div class="brand" style="left:482px;top:60px"><b></b>TOLVANE</div>

<nav class="nav">
  <a class="on" style="width:108px">Home</a>
  <a style="width:123px">About us</a>
  <a style="width:123px">Services</a>
  <a style="width:140px">Categories</a>
  <a style="width:150px">Testimonials</a>
  <a style="width:104px">Blogs</a>
  <a style="width:140px;border:none">Contact us</a>
  <a class="quote">Get A Quote</a>
</nav>

<div class="ph hero" role="img" aria-label="Technician in hard hat servicing a wall-mounted split system air conditioner"></div>
<h1 class="abs head hero-title" style="font-weight:400">Air conditoning Repair &amp;<br>Electrical Service</h1>
<p class="abs hero-text">Lorem Ipsum is simply dummy text of the printing and type setting industry. Lorem Ipsum has been the industry's</p>
<div class="btn" style="left:713px;top:470px">Read More</div>
<svg class="abs" style="left:590px;top:578px" width="30" height="8"><circle cx="4" cy="4" r="3" fill="#333"/><circle cx="15" cy="4" r="3" fill="#333"/><circle cx="26" cy="4" r="3" fill="#333"/></svg>
<svg class="abs" style="left:1038px;top:568px" width="84" height="20"><path d="M2 10h34M2 10l8-7M2 10l8 7" stroke="#333" stroke-width="2" fill="none"/><path d="M48 10h34M82 10l-8-7M82 10l-8 7" stroke="#999" stroke-width="2" fill="none"/></svg>

<h2 class="abs head section-title" style="left:81px;top:706px;font-weight:400">ABOUT</h2>
<div class="abs" style="left:81px;top:755px;width:110px;height:2px;background:#333"></div>
<div class="abs about-text">
  <p>With over 17 years' experience in the Electrical Industry, Tolvane Electrical provides a superior level of knowledge, a broad range of products and a high standard of customer service.</p>
  <p>To provide our customers with an immediate response within their timeframe, and deliver on-time, every time. Our friendly tradesmen are always professionally attired and treat your home or business with respect - we leave our jobs clean and tidy.</p>
</div>
<div class="btn" style="left:81px;top:951px">Read More</div>
<div class="abs about-frame"></div>
<div class="ph" style="left:615px;top:686px;width:491px;height:326px;background:linear-gradient(135deg,#8a6a4e,#4f6f8a 60%,#c9b9a0)" role="img" aria-label="Tool bag with gloves and air conditioning pressure gauges"></div>

<h2 class="abs head section-title" style="left:0;top:1076px;width:1210px;text-align:center;font-weight:400">Service</h2>
<div class="ph svc" style="left:81px;background:linear-gradient(135deg,#9aa3ad,#3b4550)" role="img" aria-label="Rows of circuit breakers in a switchboard"></div>
<div class="ph svc" style="left:347px;background:linear-gradient(135deg,#6f6a64,#b7b0a7)" role="img" aria-label="Commercial office corridor with glass partitions"></div>
<div class="ph svc" style="left:612px;background:linear-gradient(135deg,#2d5d8c,#b9c94a)" role="img" aria-label="Industrial engineer in hard hat at a control computer"></div>
<div class="ph svc" style="left:879px;background:linear-gradient(135deg,#8d99a4,#c2a585)" role="img" aria-label="Technician installing split system with gauges"></div>
<div class="abs head svc-label" style="left:74px">Domestic</div>
<div class="abs head svc-label" style="left:355px">Commercial</div>
<div class="abs head svc-label" style="left:622px">Industrial</div>
<div class="abs head svc-label" style="left:890px">Split System<br>Installations</div>
<div class="btn" style="left:515px;top:1461px">View More</div>

<section class="abs cats">
  <h2 class="head">Service Categories</h2>
  <ul class="cat-col" style="left:82px">
    <li><svg width="20" height="20" viewBox="0 0 20 20"><circle cx="10" cy="10" r="8" fill="none" stroke="#fff" stroke-width="2"/><path d="M6 10l3 3 7-8" fill="none" stroke="#fff" stroke-width="2"/></svg>Air Conditioning</li>
    <li><svg width="20" height="20" viewBox="0 0 20 20"><circle cx="10" cy="10" r="8" fill="none" stroke="#fff" stroke-width="2"/><path d="M6 10l3 3 7-8" fill="none" stroke="#fff" stroke-width="2"/></svg>Reverse Cycle</li>
    <li><svg width="20" height="20" viewBox="0 0 20 20"><circle cx="10" cy="10" r="8" fill="none" stroke="#fff" stroke-width="2"/><path d="M6 10l3 3 7-8" fill="none" stroke="#fff" stroke-width="2"/></svg>Split System</li>
    <li><svg width="20" height="20" viewBox="0 0 20 20"><circle cx="10" cy="10" r="8" fill="none" stroke="#fff" stroke-width="2"/><path d="M6 10l3 3 7-8" fill="none" stroke="#fff" stroke-width="2"/></svg>Installation</li>
    <li><svg width="20" height="20" viewBox="0 0 20 20"><circle cx="10" cy="10" r="8" fill="none" stroke="#fff" stroke-width="2"/><path d="M6 10l3 3 7-8" fill="none" stroke="#fff" stroke-width="2"/></svg>Evaporative Cooling</li>
    <li><svg width="20" height="20" viewBox="0 0 20 20"><circle cx="10" cy="10" r="8" fill="none" stroke="#fff" stroke-width="2"/><path d="M6 10l3 3 7-8" fill="none" stroke="#fff" stroke-width="2"/></svg>Repairs &amp; Maintenance</li>
    <li><svg width="20" height="20" viewBox="0 0 20 20"><circle cx="10" cy="10" r="8" fill="none" stroke="#fff" stroke-width="2"/><path d="M6 10l3 3 7-8" fill="none" stroke="#fff" stroke-width="2"/></svg>Ducted</li>
    <li><svg width="20" height="20" viewBox="0 0 20 20"><circle cx="10" cy="10" r="8" fill="none" stroke="#fff" stroke-width="2"/><path d="M6 10l3 3 7-8" fill="none" stroke="#fff" stroke-width="2"/></svg>Air Conditioners</li>
    <li><svg width="20" height="20" viewBox="0 0 20 20"><circle cx="10" cy="10" r="8" fill="none" stroke="#fff" stroke-width="2"/><path d="M6 10l3 3 7-8" fill="none" stroke="#fff" stroke-width="2"/></svg>Appliance Repairs</li>
    <li><svg width="20" height="20" viewBox="0 0 20 20"><circle cx="10" cy="10" r="8" fill="none" stroke="#fff" stroke-width="2"/><path d="M6 10l3 3 7-8" fill="none" stroke="#fff" stroke-width="2"/></svg>Air Conditioners</li>
  </ul>
  <ul class="cat-col" style="left:489px">
    <li><svg width="20" height="20" viewBox="0 0 20 20"><circle cx="10" cy="10" r="8" fill="none" stroke="#fff" stroke-width="2"/><path d="M6 10l3 3 7-8" fill="none" stroke="#fff" stroke-width="2"/></svg>Electricians</li>
    <li><svg width="20" height="20" viewBox="0 0 20 20"><circle cx="10" cy="10" r="8" fill="none" stroke="#fff" stroke-width="2"/><path d="M6 10l3 3 7-8" fill="none" stroke="#fff" stroke-width="2"/></svg>Home Entertainment System</li>
    <li><svg width="20" height="20" viewBox="0 0 20 20"><circle cx="10" cy="10" r="8" fill="none" stroke="#fff" stroke-width="2"/><path d="M6 10l3 3 7-8" fill="none" stroke="#fff" stroke-width="2"/></svg>Security Lighting</li>
    <li><svg width="20" height="20" viewBox="0 0 20 20"><circle cx="10" cy="10" r="8" fill="none" stroke="#fff" stroke-width="2"/><path d="M6 10l3 3 7-8" fill="none" stroke="#fff" stroke-width="2"/></svg>Data Cabling</li>
    <li><svg width="20" height="20" viewBox="0 0 20 20"><circle cx="10" cy="10" r="8" fill="none" stroke="#fff" stroke-width="2"/><path d="M6 10l3 3 7-8" fill="none" stroke="#fff" stroke-width="2"/></svg>Safety Switches</li>
    <li><svg width="20" height="20" viewBox="0 0 20 20"><circle cx="10" cy="10" r="8" fill="none" stroke="#fff" stroke-width="2"/><path d="M6 10l3 3 7-8" fill="none" stroke="#fff" stroke-width="2"/></svg>Test &amp; Tag</li>
    <li><svg width="20" height="20" viewBox="0 0 20 20"><circle cx="10" cy="10" r="8" fill="none" stroke="#fff" stroke-width="2"/><path d="M6 10l3 3 7-8" fill="none" stroke="#fff" stroke-width="2"/></svg>Lighting</li>
    <li><svg width="20" height="20" viewBox="0 0 20 20"><circle cx="10" cy="10" r="8" fill="none" stroke="#fff" stroke-width="2"/><path d="M6 10l3 3 7-8" fill="none" stroke="#fff" stroke-width="2"/></svg>Rewiring</li>
    <li><svg width="20" height="20" viewBox="0 0 20 20"><circle cx="10" cy="10" r="8" fill="none" stroke="#fff" stroke-width="2"/><path d="M6 10l3 3 7-8" fill="none" stroke="#fff" stroke-width="2"/></svg>Solar Power</li>
    <li><svg width="20" height="20" viewBox="0 0 20 20"><circle cx="10" cy="10" r="8" fill="none" stroke="#fff" stroke-width="2"/><path d="M6 10l3 3 7-8" fill="none" stroke="#fff" stroke-width="2"/></svg>24/7 Emergency Electricians</li>
  </ul>
  <ul class="cat-col" style="left:903px">
    <li><svg width="20" height="20" viewBox="0 0 20 20"><circle cx="10" cy="10" r="8" fill="none" stroke="#fff" stroke-width="2"/><path d="M6 10l3 3 7-8" fill="none" stroke="#fff" stroke-width="2"/></svg>Repairs</li>
    <li><svg width="20" height="20" viewBox="0 0 20 20"><circle cx="10" cy="10" r="8" fill="none" stroke="#fff" stroke-width="2"/><path d="M6 10l3 3 7-8" fill="none" stroke="#fff" stroke-width="2"/></svg>Renovations</li>
    <li><svg width="20" height="20" viewBox="0 0 20 20"><circle cx="10" cy="10" r="8" fill="none" stroke="#fff" stroke-width="2"/><path d="M6 10l3 3 7-8" fill="none" stroke="#fff" stroke-width="2"/></svg>Power Points</li>
    <li><svg width="20" height="20" viewBox="0 0 20 20"><circle cx="10" cy="10" r="8" fill="none" stroke="#fff" stroke-width="2"/><path d="M6 10l3 3 7-8" fill="none" stroke="#fff" stroke-width="2"/></svg>New Installations</li>
    <li><svg width="20" height="20" viewBox="0 0 20 20"><circle cx="10" cy="10" r="8" fill="none" stroke="#fff" stroke-width="2"/><path d="M6 10l3 3 7-8" fill="none" stroke="#fff" stroke-width="2"/></svg>New Homes</li>
    <li><svg width="20" height="20" viewBox="0 0 20 20"><circle cx="10" cy="10" r="8" fill="none" stroke="#fff" stroke-width="2"/><path d="M6 10l3 3 7-8" fill="none" stroke="#fff" stroke-width="2"/></svg>Switchboards</li>
    <li><svg width="20" height="20" viewBox="0 0 20 20"><circle cx="10" cy="10" r="8" fill="none" stroke="#fff" stroke-width="2"/><path d="M6 10l3 3 7-8" fill="none" stroke="#fff" stroke-width="2"/></svg>Hot Water Systems</li>
    <li><svg width="20" height="20" viewBox="0 0 20 20"><circle cx="10" cy="10" r="8" fill="none" stroke="#fff" stroke-width="2"/><path d="M6 10l3 3 7-8" fill="none" stroke="#fff" stroke-width="2"/></svg>Electric</li>
  </ul>
</section>

<div class="abs" style="left:0;top:2142px;width:1195px;text-align:center;font-size:14px">Testimonials</div>
<h2 class="abs head section-title" style="left:0;top:2168px;width:1225px;text-align:center;font-weight:400">What Client Say</h2>

<div class="abs t-card" style="left:81px">
  <div class="avatar" style="background:#9a9a9a" role="img" aria-label="Client portrait"></div>
  <div class="name">Marcus</div><div class="role">Director</div>
  <div class="quote">Lorem Ipsum is simply dummy of the printing and typesetting Lorem Ipsum industry.</div>
  <div class="more">Read More... <svg width="16" height="16"><circle cx="8" cy="8" r="6.5" fill="none" stroke="#444"/><path d="M7 5l3 3-3 3" fill="none" stroke="#444"/></svg></div>
</div>
<div class="abs t-card" style="left:446px">
  <div class="avatar" style="background:#b07a62" role="img" aria-label="Client portrait"></div>
  <div class="name">Sophie</div><div class="role">Director</div>
  <div class="quote bold">Lorem Ipsum is simply dummy of the printing and typesetting Lorem Ipsum industry.</div>
  <div class="more">Read More... <svg width="16" height="16"><circle cx="8" cy="8" r="6.5" fill="none" stroke="#444"/><path d="M7 5l3 3-3 3" fill="none" stroke="#444"/></svg></div>
</div>
<div class="abs t-card" style="left:803px">
  <div class="avatar" style="background:#6f7f8f" role="img" aria-label="Client portrait"></div>
  <div class="name">Liam Carter</div><div class="role">Director</div>
  <div class="quote">Lorem Ipsum is simply dummy of the printing and typesetting Lorem Ipsum industry.</div>
  <div class="more">Read More... <svg width="16" height="16"><circle cx="8" cy="8" r="6.5" fill="none" stroke="#444"/><path d="M7 5l3 3-3 3" fill="none" stroke="#444"/></svg></div>
</div>
<svg class="abs" style="left:582px;top:2590px" width="36" height="10"><circle cx="5" cy="5" r="4" fill="#222"/><circle cx="18" cy="5" r="4" fill="#aaa"/><circle cx="31" cy="5" r="4" fill="#aaa"/></svg>

<h2 class="abs head section-title" style="left:0;top:2638px;width:1200px;text-align:center;font-weight:400">Blogs</h2>

<div class="abs b-card" style="left:81px">
  <div class="img" style="background:linear-gradient(135deg,#9a6c4a,#3d5e86)" role="img" aria-label="Technician testing an outdoor unit with gauges"></div>
  <div class="link"><svg width="20" height="20" viewBox="0 0 20 20"><path d="M8 12l4-4M7 9l-2 2a3 3 0 0 0 4 4l2-2M13 11l2-2a3 3 0 0 0-4-4L9 7" fill="none" stroke="#fff" stroke-width="2"/></svg></div>
  <div class="row"><span class="t">Blog # 1</span><span class="d">June 04.2019</span></div>
  <div class="txt">Lorem Ipsum is simply an dummy text of the printing and typesetting industry.</div>
  <div class="foot"><u>Read Full Artcle</u><div class="stats"><span>♡ 35</span><span>○ 20</span></div></div>
</div>
<div class="abs b-card" style="left:449px">
  <div class="img" style="background:linear-gradient(135deg,#8a8276,#2f2f2f)" role="img" aria-label="Worker cleaning an air conditioner coil"></div>
  <div class="link"><svg width="20" height="20" viewBox="0 0 20 20"><path d="M8 12l4-4M7 9l-2 2a3 3 0 0 0 4 4l2-2M13 11l2-2a3 3 0 0 0-4-4L9 7" fill="none" stroke="#fff" stroke-width="2"/></svg></div>
  <div class="row"><span class="t">Blog # 1</span><span class="d">June 04.2019</span></div>
  <div class="txt">Lorem Ipsum is simply an dummy text of the printing and typesetting industry.</div>
  <div class="foot"><u>Read Full Artcle</u><div class="stats"><span>♡ 35</span><span>○ 20</span></div></div>
</div>
<div class="abs b-card" style="left:801px">
  <div class="img" style="background:linear-gradient(135deg,#f1f1f1,#c9c9c9 60%,#d8b24a)" role="img" aria-label="Technician servicing a wall split system"></div>
  <div class="link"><svg width="20" height="20" viewBox="0 0 20 20"><path d="M8 12l4-4M7 9l-2 2a3 3 0 0 0 4 4l2-2M13 11l2-2a3 3 0 0 0-4-4L9 7" fill="none" stroke="#fff" stroke-width="2"/></svg></div>
  <div class="row"><span class="t">Blog # 1</span><span class="d">June 04.2019</span></div>
  <div class="txt">Lorem Ipsum is simply an dummy text of the printing and typesetting industry.</div>
  <div class="foot"><u>Read Full Artcle</u><div class="stats"><span>♡ 35</span><span>○ 20</span></div></div>
</div>
<div class="btn" style="left:515px;top:3128px">View More</div>

<section class="abs contact">
  <h2 class="head">Quick Contact</h2>
  <div class="field" style="left:80px;top:131px;width:224px">First Name</div>
  <div class="field" style="left:316px;top:131px;width:225px">Last Name</div>
  <div class="field" style="left:80px;top:177px;width:224px">Email</div>
  <div class="field" style="left:316px;top:177px;width:225px">Phone</div>
  <div class="field" style="left:80px;top:222px;width:461px;height:108px">Message</div>
  <div class="btn" style="left:80px;top:360px;background:var(--red);width:174px">Submit</div>
</section>
<div class="ph map" role="img" aria-label="Street map showing the business location"></div>
<svg class="abs" style="left:741px;top:3247px" width="28" height="40" viewBox="0 0 28 40"><path d="M14 0a14 14 0 0 1 14 14c0 10-14 26-14 26S0 24 0 14A14 14 0 0 1 14 0z" fill="var(--red)"/><circle cx="14" cy="14" r="5" fill="#a01014"/></svg>
<div class="abs map-card">
  <svg width="12" height="14" viewBox="0 0 12 14" style="position:absolute;left:34px;top:19px"><path d="M6 1a4.5 4.5 0 0 1 4.5 4.5C10.5 9 6 13 6 13S1.5 9 1.5 5.5A4.5 4.5 0 0 1 6 1z" fill="none" stroke="#333"/><circle cx="6" cy="5.5" r="1.5" fill="#333"/></svg>
  <div>48 Harbour Lane,</div>
  <div>Westbrook, USA</div>
  <div>+123 555 0142</div>
</div>

<footer class="abs footer">
  <div class="brand" style="left:80px;top:58px;font-size:36px;color:#fff"><b style="width:30px;height:30px"></b>TOLVANE</div>
  <p class="abs" style="left:81px;top:149px;width:250px;font-size:12.5px;line-height:16px">Lorem Ipsum is simply dummy text of the Ipsum is simply dummy text of the lorum printing and typesetting industry. .</p>
  <div class="abs" style="left:81px;top:212px;font-size:13px;display:flex;gap:3px;align-items:center">Read More..<svg width="14" height="14"><circle cx="7" cy="7" r="6" fill="none" stroke="#fff"/><path d="M6 4l3 3-3 3" fill="none" stroke="#fff"/></svg></div>

  <div class="abs" style="left:370px;top:82px">
    <h4>Quick Link</h4>
    <ul><li>Home</li><li>About us</li><li>Services</li><li>Categories</li><li>Testimonials</li><li>Blogs</li><li>Contact us</li></ul>
  </div>

  <div class="abs f-contact" style="left:576px;top:82px">
    <h4 style="margin-bottom:10px">Quick Contact</h4>
    <div><svg width="14" height="16" viewBox="0 0 12 14" style="margin-top:5px"><path d="M6 1a4.5 4.5 0 0 1 4.5 4.5C10.5 9 6 13 6 13S1.5 9 1.5 5.5A4.5 4.5 0 0 1 6 1z" fill="none" stroke="#fff"/><circle cx="6" cy="5.5" r="1.5" fill="#fff"/></svg><span>48 Harbour Lane<br>Westbrook, USA<br>Zip :1234</span></div>
    <div><svg width="14" height="14" viewBox="0 0 24 24" style="margin-top:6px"><path fill="none" stroke="#fff" stroke-width="2" d="M6.6 10.8a15 15 0 0 0 6.6 6.6l2.2-2.2 4.6 1.4V20A17 17 0 0 1 4 4h3.5l1.2 4.6z"/></svg>+123 555 0142</div>
    <div><svg width="14" height="12" viewBox="0 0 16 12" style="margin-top:7px"><rect x=".5" y=".5" width="15" height="11" fill="none" stroke="#fff"/><path d="M.5.5 8 7l7.5-6.5" fill="none" stroke="#fff"/></svg>info@tolvane.com</div>
  </div>

  <div class="abs" style="left:893px;top:82px">
    <h4>Subscribe</h4>
    <div style="font-size:13px;margin-top:12px">Subscribe For Our Newsletter</div>
    <div class="subscribe"><span>Email Address</span><b>Subscribe</b></div>
    <div class="socials"><i></i><i></i><i></i><i></i></div>
  </div>

  <nav class="abs web-links">
    <a href="https://tolvane.com.au">tolvane.com.au</a>
    <a href="https://tolvaneelectrical.com.au">tolvaneelectrical.com.au</a>
    <a href="https://tolvaneairandelectrical.com.au">tolvaneairandelectrical.com.au</a>
    <a href="https://tolvaneair.com.au">tolvaneair.com.au</a>
  </nav>
</footer>
<div class="abs bottom">
  <span class="abs" style="left:81px;top:20px">CopyRight©2019 Tolvane Air and Electrical. All Right Reserve</span>
  <span class="abs" style="right:80px;top:18px">Privacy Policy - Terms &amp; Conditions</span>
</div>

</body>
</html>
```